Book Cover Design Project

I have written a booK called "Build From Nothing:
a handbook for launching and steering a modest enterprise. It is aimed at the start up entrepreneur and seeks to give them everything they need to start up and run a small business. I am interested in a very simple cover that is contemporary in the look but clearly communicates the mission of the book. It should sell very well as there are no others like it, so the designer will get excellent exposure.
Updates

Reason: I an vacation in Europe until the 23rd of July. Would like a few days to make a decision after my return Ned

We are currently on vacation.  Will make a final decision in about a week.  Thanks so much for your submissions

Ned

Target Market(s)

Start up businesses in the U.S.

Industry/Entity Type

Business

Requirements
Must have
• Clear communication of the name. Lots of white space. Graphic communication of the purpose of the book? Prominent exposure of my name. Edward r. Kistlewood

```html
<!DOCTYPE html>
<html lang="en">
<head>
<meta charset="utf-8">
<title>Build From Nothing — Book Cover</title>
<link rel="stylesheet" href="https://fonts.googleapis.com/css2?family=Montserrat:wght@700;800&display=swap">
<style>
  :root {
    --cover-black: #000000;
    --title-yellow: #ebb700;
    --subtitle-grey: #76777b;
    --author-white: #ffffff;
  }
  html, body {
    margin: 0;
    padding: 0;
    width: 800px;
    height: 1200px;
    overflow: hidden;
    background: var(--cover-black);
  }
  .cover {
    position: relative;
    width: 800px;
    height: 1200px;
    background: var(--cover-black);
    font-family: "Montserrat", Arial, sans-serif;
    font-weight: 700;
  }
  .author {
    position: absolute;
    top: 62px;
    left: 0;
    width: 100%;
    margin: 0;
    text-align: center;
    color: var(--author-white);
    font-size: 26px;
    letter-spacing: 2.5px;
  }
  .title {
    position: absolute;
    top: 282px;
    left: 80px;
    margin: 0;
    color: var(--title-yellow);
    font-size: 96px;
    font-weight: 800;
    line-height: 116px;
    letter-spacing: -1px;
    white-space: nowrap;
  }
  .title span { display: block; }
  .subtitle {
    position: absolute;
    top: 570px;
    left: 80px;
    width: 660px;
    margin: 0;
    color: var(--subtitle-grey);
    font-size: 66px;
    font-weight: 800;
    line-height: 92px;
    letter-spacing: -0.5px;
    white-space: nowrap;
  }
  .subtitle-line { display: block; }
</style>
</head>
<body>
  <main class="cover">
    <p class="author">EDWARD R. KISTLEWOOD</p>

    <h1 class="title">
      <span>BUILD FROM</span>
      <span>NOTHING!</span>
    </h1>

    <h2 class="subtitle">
      <span class="subtitle-line">A HANDBOOK FOR</span>
      <span class="subtitle-line">LAUNCHING AND</span>
      <span class="subtitle-line">STEERING A</span>
      <span class="subtitle-line">MODEST</span>
      <span class="subtitle-line">ENTERPRISE</span>
    </h2>
  </main>
</body>
</html>
```